Create branded design templates/backgrounds for social media based on UK property investing company

I'd like Instagram, Facebook and Linkedin backgrounds/templates to add text to, based on my logo design and business of UK holiday let investing. Ideally I'd have some base designs for me to approve, then engage with the winning designer further to create about 50 different templates. I looking for a mixture of templates with the logo and using logo colours, others of internal holiday let photos including logos and a few of my photo imposed on the front of them.
Updates

Slow in providing feedback

Target Market(s)

Middle aged adults

Industry/Entity Type

Holiday let properties

Requirements
Must have
• a distinct brand look that can be replicated

```html
<!DOCTYPE html>
<html lang="en">
<head>
<meta charset="utf-8">
<title>Harbourstone Lets – Social Post</title>
<link href="https://fonts.googleapis.com/css2?family=Anton&family=Raleway:wght@400;500;600&family=Mrs+Saint+Delafield&display=swap" rel="stylesheet">
<style>
  :root {
    --backdrop: #373737;
    --brand-green: #58a80a;
    --photo-light: #c9dcc0;
    --photo-mid: #8fb879;
    --white: #ffffff;
    --accent-yellow: #f6dd3a;
    --brand-blue: #1a77c4;
    --ink: #2b2b2b;
    --tab-shadow: #cfcfd4;
  }
  * { margin: 0; padding: 0; box-sizing: border-box; }
  html, body { width: 1197px; height: 1200px; overflow: hidden; background: var(--backdrop); }
  .canvas { position: relative; width: 1197px; height: 1200px; background: var(--backdrop); }
  .post {
    position: absolute; left: 128px; top: 128px; width: 942px; height: 942px;
    background: var(--brand-green); overflow: hidden;
  }
  .hero-photo {
    position: absolute; left: 0; top: 0; width: 942px; height: 560px;
    background: linear-gradient(180deg, var(--photo-light) 0%, var(--photo-mid) 55%, var(--brand-green) 100%);
  }
  .brand-tab {
    position: absolute; left: 0; top: 0; width: 236px; height: 178px;
    background: var(--white); border-bottom-right-radius: 60px;
    box-shadow: 6px 8px 0 var(--tab-shadow);
    display: flex; align-items: center; padding-left: 26px; gap: 9px;
  }
  .brand-mark { width: 16px; height: 16px; background: var(--brand-blue); border-radius: 50%; flex: none; }
  .brand-name { font-family: "Raleway", sans-serif; font-weight: 600; font-size: 17px; color: var(--ink); line-height: 1.1; }
  .halftone { position: absolute; }
  .halftone--top { right: 0; top: 0; width: 116px; height: 134px; background: radial-gradient(circle at 100% 0%, rgba(255,255,255,0.55), rgba(255,255,255,0) 70%); }
  .halftone--bottom { left: 0; bottom: 0; width: 95px; height: 146px; background: radial-gradient(circle at 0% 100%, rgba(246,221,58,0.8), rgba(246,221,58,0) 72%); }
  .corner-swoosh { position: absolute; right: 0; bottom: 0; width: 72px; height: 186px; }
  .headline {
    position: absolute; left: 0; top: 352px; width: 942px; text-align: center;
    font-family: "Anton", sans-serif; color: var(--white); font-size: 124px; line-height: 112px;
    text-transform: uppercase; letter-spacing: 1px;
  }
  .underline { position: absolute; left: 151px; top: 623px; width: 326px; height: 7px; background: var(--accent-yellow); border-radius: 4px; }
  .tagline-script {
    position: absolute; left: 505px; top: 566px;
    font-family: "Mrs Saint Delafield", cursive; color: var(--accent-yellow); font-size: 96px; line-height: 1;
  }
  .intro {
    position: absolute; left: 0; top: 683px; width: 942px; text-align: center;
    font-family: "Raleway", sans-serif; color: var(--white); font-size: 21px; line-height: 33px;
  }
  .contact-bar {
    position: absolute; left: 146px; top: 781px; width: 649px; height: 81px;
    background: var(--white); border-radius: 22px;
    display: flex; align-items: center; padding-left: 42px;
  }
  .contact-icon { width: 38px; height: 38px; flex: none; }
  .contact-label { font-family: "Anton", sans-serif; color: var(--brand-blue); font-size: 36px; margin-left: 14px; letter-spacing: 0.5px; }
  .divider-dots { display: flex; flex-direction: column; gap: 4px; margin-left: 46px; margin-right: 28px; }
  .divider-dots span { width: 8px; height: 8px; border-radius: 50%; background: var(--brand-green); }
  .contact-url { font-family: "Raleway", sans-serif; font-weight: 500; color: var(--ink); font-size: 22px; }
</style>
</head>
<body>
<div class="canvas">
  <div class="post">
    <div class="hero-photo" role="img" aria-label="Photo of a model house under construction with exposed roof timbers, resting on rolled architectural blueprints, tinted green"></div>
    <div class="halftone halftone--top" role="img" aria-label="White halftone dot pattern"></div>
    <div class="halftone halftone--bottom" role="img" aria-label="Yellow halftone dot pattern"></div>
    <svg class="corner-swoosh" viewBox="0 0 72 186" aria-hidden="true">
      <path d="M72 30 C 20 70, 0 120, 40 186 L72 186 Z" fill="var(--accent-yellow)"/>
      <path d="M72 50 C 30 90, 18 135, 52 186 L72 186 Z" fill="var(--brand-blue)"/>
    </svg>
    <div class="brand-tab">
      <span class="brand-mark"></span>
      <span class="brand-name">Harbourstone Lets</span>
    </div>
    <h1 class="headline">The Smartest<br>Way to Invest</h1>
    <div class="underline"></div>
    <div class="tagline-script">With Us</div>
    <p class="intro">Build your dream house with us! Our expert team will guide<br>you every step of the way. Contact us now!</p>
    <div class="contact-bar">
      <svg class="contact-icon" viewBox="0 0 38 38" aria-hidden="true">
        <circle cx="19" cy="19" r="19" fill="var(--brand-blue)"/>
        <rect x="9" y="12" width="20" height="14" rx="2" fill="var(--white)"/>
        <path d="M9.5 13 L19 20.5 L28.5 13" fill="none" stroke="var(--brand-blue)" stroke-width="1.8"/>
      </svg>
      <span class="contact-label">CONTACT US</span>
      <div class="divider-dots"><span></span><span></span><span></span></div>
      <span class="contact-url">www.harbourstonelets.com</span>
    </div>
  </div>
</div>
</body>
</html>
```